Chimney Service company needs new business card design

We need a updated business card with our new logo added. We provide a full range of chimney services throughout Vermont and New Hampshire. The business card will be one sided and color. Attached is our current business card another document showing all the information we would like on the card.
We dont like a lot of flashy colors.... here is a link to our website to get an idea of our branding www.flueguardianvt.example

Target Market(s)

homeowners

Industry/Entity Type

Business

Contact Information for Business Card

See attached sheet for content.

Font styles to use
Serif
Sans Serif

Requirements
Must have
• all information provided on separate sheet
Should not have
• Additional information that may clogg up design

```html
<!DOCTYPE html>
<html lang="en">
<head>
<meta charset="utf-8">
<title>Flue Guardian – Business Card</title>
<link href="https://fonts.googleapis.com/css2?family=Cinzel:wght@400;600&display=swap" rel="stylesheet">
<style>
  :root {
    --backdrop: #d6d6d6;
    --card: #ffffff;
    --ink: #1f1f1f;
    --accent: #a30f14;
    --rule: #2a2a2a;
  }
  * { margin: 0; padding: 0; box-sizing: border-box; }
  html, body {
    width: 1200px; height: 1000px; overflow: hidden;
    background: var(--backdrop);
    font-family: "Cinzel", "Times New Roman", serif;
  }
  .card {
    position: absolute; left: 150px; top: 243px;
    width: 900px; height: 514px;
    background: var(--card);
    box-shadow: 0 6px 22px rgba(0,0,0,.18);
    color: var(--ink);
  }
  .accent-bar { position: absolute; background: var(--accent); }
  .accent-bar--left { left: 22px; top: 220px; width: 50px; height: 118px; }
  .accent-bar--right { right: 0; top: 118px; width: 50px; height: 134px; }

  .brand {
    position: absolute; left: 0; right: 0; top: 48px;
    display: flex; justify-content: center; align-items: center; gap: 16px;
  }
  .brand__mark { width: 48px; height: 48px; background: var(--rule); }
  .brand__name { font-size: 40px; font-weight: 600; letter-spacing: 1px; color: var(--ink); }
  .tagline {
    position: absolute; left: 0; right: 0; top: 118px;
    text-align: center; font-size: 13px; letter-spacing: .5px;
  }

  .contact {
    position: absolute; right: 472px; top: 232px;
    text-align: right; font-size: 16px; line-height: 24px; font-style: normal;
  }
  .contact__row { display: flex; justify-content: flex-end; align-items: center; gap: 6px; }
  .contact__icon { width: 14px; height: 14px; }

  .divider {
    position: absolute; left: 448px; top: 192px;
    width: 2px; height: 138px; background: var(--accent);
  }

  .services { position: absolute; left: 470px; top: 192px; }
  .services__title { font-size: 19px; color: var(--accent); font-weight: 600; margin-bottom: 4px; }
  .services__list { list-style: none; font-size: 15px; line-height: 21px; }
  .services__list li { display: flex; align-items: center; gap: 7px; }
  .services__list li::before {
    content: ""; width: 7px; height: 7px; border-radius: 50%; background: var(--accent);
  }

  .assurances {
    position: absolute; left: 0; right: 0; top: 420px;
    display: flex; justify-content: center; align-items: center; gap: 16px;
    font-size: 18px; font-weight: 600; color: var(--accent);
  }
  .assurances__dot { width: 8px; height: 8px; border-radius: 50%; background: var(--ink); }
</style>
</head>
<body>
  <main class="card">
    <div class="accent-bar accent-bar--left"></div>
    <div class="accent-bar accent-bar--right"></div>

    <header class="brand">
      <span class="brand__mark"></span>
      <span class="brand__name">FLUE GUARDIAN</span>
    </header>
    <p class="tagline">Serving VT and New Hampshire since 1989</p>

    <address class="contact">
      <div class="contact__row">802-555-0147
        <svg class="contact__icon" viewBox="0 0 16 16"><path fill="#a30f14" d="M3 1l3 3-1.5 2a9 9 0 0 0 5.5 5.5L12 10l3 3-2 2C7 15 1 9 1 3z"/></svg>
      </div>
      <div class="contact__row">info@flueguardianvt.example
        <svg class="contact__icon" viewBox="0 0 16 16"><rect x="1" y="3" width="14" height="10" fill="#a30f14"/><path d="M1 3l7 6 7-6" fill="none" stroke="#fff" stroke-width="1.3"/></svg>
      </div>
      <div class="contact__row">www.flueguardianvt.example
        <svg class="contact__icon" viewBox="0 0 16 16"><circle cx="8" cy="8" r="7" fill="#a30f14"/><path d="M1 8h14M8 1v14M3 4h10M3 12h10" stroke="#fff" stroke-width="1" fill="none"/><ellipse cx="8" cy="8" rx="3" ry="7" fill="none" stroke="#fff" stroke-width="1"/></svg>
      </div>
    </address>

    <div class="divider"></div>

    <section class="services">
      <h2 class="services__title">Services we provide</h2>
      <ul class="services__list">
        <li>Full Masonry Services</li>
        <li>Historic chimney restoration</li>
        <li>Stainless steel liners</li>
        <li>New Chimney installations</li>
        <li>FSTB Certified Chimney sweeps</li>
      </ul>
    </section>

    <footer class="assurances">
      <span>Fully Insured – Free Estimates</span>
      <span class="assurances__dot"></span>
      <span>Family owned and operated</span>
    </footer>
  </main>
</body>
</html>
```